Visitenkarten-Design für K17.eu - TradeWing Finanz
Zielgruppe
Smartphone-Banking mit Mehrwert
Aufgabenstellung
Bitte entwerfen Sie kreative Visitenkarten für uns.
- Halten Sie einen Platz/Rahmen frei für Fotos, die wir nachträglich einsetzen, und kennzeichnen diesen.
- Halten Sie einen Patz/Rahmen für Vor- und Nachname sowie für die Berufsbezeichnung frei und kennzeichnen diesen.
- Halten Sie einen Platz/Rahmen für die Telefonnummern und die Email-Adressen frei und kennzeichnen diesen.
Alle Visitenkarten sollen folgende Daten beinhalten:
Vorname Nachname*
Berufsbezeichnung*
Mobile:
Office:
Email:
Domain:
* = individuell, jeder Mitarbeiter hat eigene Daten
Die Farben müssen sich an unserem CI-Design orientieren, orange/weiß/schwarz/grau -
Außerdem finden Sie unser Logo in der Anlage, welches Sie bitte auf der Karte platzieren.
Bitte liefern Sie uns die Designs in verschiedenen Formaten - psd, ai, eps, jpg, png
Bei Fragen zögern Sie nicht, uns zu kontaktieren. Danke.

```html
<!DOCTYPE html>
<html lang="de">
<head>
<meta charset="utf-8">
<title>K17.eu – Visitenkarten</title>
<link rel="stylesheet" href="https://fonts.googleapis.com/css2?family=Open+Sans:wght@400;600;700&display=swap">
<style>
  :root {
    --orange: #ec6613;
    --grey: #626161;
    --white: #ffffff;
    --ink: #222222;
    --stage: #e9e6e2;
    --photo-a: #d9d6d2;
    --photo-b: #b9b7b4;
  }
  * { box-sizing: border-box; margin: 0; padding: 0; }
  html, body {
    width: 1200px; height: 822px; overflow: hidden;
    background: var(--stage);
    font-family: "Open Sans", Arial, sans-serif;
  }
  .stage { position: relative; width: 1200px; height: 822px; }

  .card {
    position: absolute; width: 560px; height: 320px;
    box-shadow: 0 10px 28px rgba(0,0,0,.22);
    overflow: hidden;
  }

  /* Rückseite */
  .card-back { left: 90px; top: 70px; background: var(--grey); }
  .card-back .brand {
    position: absolute; left: 0; right: 0; top: 112px;
    display: flex; justify-content: center; align-items: center; gap: 18px;
  }
  .brand-mark { width: 34px; height: 34px; background: var(--orange); }
  .brand-name {
    font-weight: 700; font-size: 62px; letter-spacing: 1px;
    color: var(--white); line-height: 1;
  }
  .card-back .domain {
    position: absolute; left: 0; right: 0; top: 240px; text-align: center;
    font-size: 15px; letter-spacing: 1px; color: var(--white);
  }

  /* Vorderseite */
  .card-front { left: 550px; top: 432px; display: flex; background: var(--white); }
  .front-info {
    width: 262px; height: 100%; background: var(--orange);
    padding: 34px 0 0 30px; color: var(--white);
  }
  .front-info .brand { display: flex; align-items: center; gap: 10px; }
  .front-info .brand-mark { width: 20px; height: 20px; background: var(--white); }
  .front-info .brand-name { font-size: 38px; }
  .front-stripe { width: 16px; height: 100%; background: var(--grey); }
  .address { margin-top: 56px; font-size: 13px; line-height: 1.4; }
  .contacts { list-style: none; margin-top: 10px; font-size: 13px; line-height: 1.55; }
  .contacts li { display: flex; align-items: center; gap: 10px; }
  .contacts svg { width: 13px; height: 13px; flex: none; }

  .front-person { flex: 1; padding: 26px 26px 0 30px; }
  .person-name { font-size: 24px; font-weight: 700; color: var(--orange); line-height: 1.1; }
  .person-role { font-size: 13px; color: var(--ink); margin-top: 2px; }
  .photo-frame {
    margin-top: 16px; width: 220px; height: 210px;
    border: 1.5px solid var(--orange); border-radius: 8px; padding: 4px;
  }
  .photo-slot {
    width: 100%; height: 100%; border-radius: 5px;
    background: linear-gradient(160deg, var(--photo-a), var(--photo-b));
  }
</style>
</head>
<body>
<main class="stage">

  <section class="card card-back" aria-label="Visitenkarte Rückseite">
    <div class="brand">
      <span class="brand-mark"></span>
      <span class="brand-name">K17.eu</span>
    </div>
    <p class="domain">www.k17.eu</p>
  </section>

  <section class="card card-front" aria-label="Visitenkarte Vorderseite">
    <div class="front-info">
      <div class="brand">
        <span class="brand-mark"></span>
        <span class="brand-name">K17.eu</span>
      </div>
      <p class="address">K17 GmbH<br>Lindenstr. 12<br>93047 Regensburg, Germany</p>
      <ul class="contacts">
        <li>
          <svg viewBox="0 0 14 14" fill="none" stroke="#fff" stroke-width="1.4"><rect x="3.5" y="1" width="7" height="12" rx="1.2"/><line x1="6" y1="11" x2="8" y2="11"/></svg>
          + 49 160 7654321
        </li>
        <li>
          <svg viewBox="0 0 14 14" fill="#fff"><path d="M3 1l2.5 2.8-1.3 1.6c.8 1.8 2.2 3.2 4 4l1.6-1.3L12.6 10.6 11 13C6 12.4 1.6 8 1 3z"/></svg>
          + 49 941 765432-00
        </li>
        <li>
          <svg viewBox="0 0 14 14" fill="none" stroke="#fff" stroke-width="1.4"><rect x="1" y="3" width="12" height="8"/><polyline points="1,3 7,8 13,3"/></svg>
          jonas@k17.eu
        </li>
        <li>
          <svg viewBox="0 0 14 14" fill="none" stroke="#fff" stroke-width="1.4"><circle cx="7" cy="7" r="5.8"/><ellipse cx="7" cy="7" rx="2.4" ry="5.8"/><line x1="1.2" y1="7" x2="12.8" y2="7"/></svg>
          www.k17.eu
        </li>
      </ul>
    </div>
    <div class="front-stripe"></div>
    <div class="front-person">
      <h1 class="person-name">Jonas Beispiel</h1>
      <p class="person-role">Geschäftsführer</p>
      <div class="photo-frame">
        <div class="photo-slot" role="img" aria-label="Platz für das Porträtfoto der Person"></div>
      </div>
    </div>
  </section>

</main>
</body>
</html>
```